An Engineering & Procurement Company Needs a Brochure Design

We need brochure design (company profile) for our company: VERTANEX®, the company procures and supplies products such as Valves and Actuators, Flanges and Pipe Fittings, Piping and Structural, Oilfield and Drilling Equipments, our After Sales and Engineering Services (VASES) includes
1. Fabrication, Machining and Repairing
2. Testing, Servicing and Commissioning of Products.
Most of the information can be found on our company's website: www.vertanex.co; if you need further information please contact us back.
Updates
Project Deadline Extended Reason: Deadline as been extended as we are yet to decide on the final design. Added Thursday, October 8, 2015
Target Market(s)
Oil & Gas, Power & Alternative Energy, Water Supply / Sewage, Industrial Process, Civil Infrastructure, General Construction and Etc.
Industry/Entity Type
Mechanical Engineering
Font styles to use
Other font styles liked:
- Google Fonts Play
Look and feel
Each slider illustrates characteristics of the customer's brand and the style your logo design should communicate.

```html
<!DOCTYPE html>
<html lang="en">
<head>
<meta charset="utf-8">
<title>VERTANEX® Company Profile Brochure</title>
<link href="https://fonts.googleapis.com/css2?family=Play:wght@400;700&display=swap" rel="stylesheet">
<style>
:root{
  --red:#d6262b;
  --red-dark:#a81c20;
  --blue:#1b4f97;
  --grey:#e7e8ea;
  --grey-mid:#cfd1d4;
  --ink:#3a3d42;
  --white:#ffffff;
}
*{box-sizing:border-box;margin:0;padding:0}
html,body{width:898px;height:1200px;overflow:hidden;background:var(--white)}
body{font-family:"Play",sans-serif;color:var(--ink);position:relative}

.spread{position:absolute;left:15px;width:868px;display:flex;box-shadow:0 1px 4px rgba(0,0,0,.25);overflow:hidden}
.spread--outer{top:15px;height:275px}
.spread--inner{top:305px;height:880px}

/* outer spread */
.back-panel{width:290px;position:relative;background:var(--grey);overflow:hidden}
.back-panel .facet{position:absolute;inset:0}
.contact-block{position:relative;background:var(--red);color:var(--white);height:170px;padding:22px 20px;font-size:10.5px;line-height:1.45;text-transform:uppercase}
.contact-block p{margin-bottom:10px}
.wordmark{display:flex;align-items:center;gap:6px;font-weight:700;font-size:16px;letter-spacing:.5px;color:var(--red)}
.wordmark .dot{width:14px;height:14px;border-radius:50%;background:var(--red)}
.back-panel .wordmark{position:absolute;left:20px;bottom:18px}

.front-panel{flex:1;position:relative;background:var(--white)}
.hero-photo{height:210px;background:linear-gradient(180deg,#1d2f55 0%,#5a4a6a 45%,#d9743a 78%,#2a1a18 100%)}
.front-panel .wordmark--badge{position:absolute;top:14px;right:16px;background:var(--white);padding:6px 10px;font-size:14px}
.front-strip{position:absolute;left:0;right:0;bottom:0;height:65px;display:flex;align-items:center;padding-left:26px}
.front-strip .facet{position:absolute;inset:0}
.front-strip .wordmark{position:relative;font-size:18px}

/* inner spread */
.col{position:relative;overflow:hidden}
.col--profile{width:290px;background:var(--grey);padding:20px 18px 0}
.col--sectors{width:270px;background:var(--white);padding:26px 20px 0}
.col--industries{flex:1;background:var(--white)}

.section-title{font-weight:700;font-size:20px;letter-spacing:.5px;text-transform:uppercase;color:var(--blue)}
.col--profile .section-title{margin-bottom:12px}
.photo{display:block;width:100%}
.photo--pipes-red{height:150px;background:linear-gradient(135deg,#8e1d1b,#c9472f 50%,#5c1512)}
.photo--pipes-steel{position:absolute;left:0;right:0;bottom:0;height:250px;background:linear-gradient(160deg,#c9ccd0,#8b9096 50%,#e2e4e6)}
.body-text{font-size:9.5px;line-height:1.45;margin-top:10px}
.product-list{list-style:none;margin-top:8px;font-size:9.5px;line-height:1.45}
.product-list li{position:relative;padding-left:12px;margin-bottom:4px}
.product-list li::before{content:"";position:absolute;left:0;top:4px;width:6px;height:6px;background:var(--red)}
.product-list strong{color:var(--blue)}
.sub-title{margin-top:10px;font-weight:700;font-size:12px;color:var(--red);line-height:1.3}

.kicker{font-size:9.5px;margin-bottom:8px}
.sector-statement{font-weight:700;font-size:22px;line-height:1.15;text-transform:uppercase;color:var(--blue);margin-bottom:16px}
.col--sectors .body-text{margin-top:12px}
.sectors-foot{position:absolute;left:0;right:0;bottom:0;height:250px;background:var(--grey)}
.sectors-foot .facet{position:absolute;inset:0}

.band{background:var(--red);color:var(--white);font-weight:700;font-size:22px;text-transform:uppercase;padding:14px 22px;letter-spacing:.5px}
.industry-grid{display:grid;grid-template-columns:1fr 1fr;gap:0 14px;padding:22px 20px}
.industry{text-align:center;height:262px}
.industry svg{width:54px;height:54px;display:block;margin:0 auto 8px}
.industry h3{font-weight:700;font-size:14px;line-height:1.15;text-transform:uppercase;color:var(--ink);margin-bottom:8px}
.industry ul{list-style:none;font-size:8.5px;line-height:1.6;text-transform:uppercase;color:#6a6e74}
</style>
</head>
<body>

<section class="spread spread--outer">
  <div class="back-panel">
    <svg class="facet" viewBox="0 0 290 275" preserveAspectRatio="none" aria-hidden="true">
      <polygon points="0,170 290,120 290,275 0,275" fill="#d9dbde"/>
      <polygon points="120,275 290,190 290,275" fill="#c9ccd0"/>
    </svg>
    <div class="contact-block">
      <p>Singapore (Global HQ)<br>Vertanex (Pte) Ltd,<br>Singapore</p>
      <p>12B Harbour Vale #02-118,<br>Avenue 4, Singapore 000000<br>Tel: +65 6000 0000</p>
    </div>
    <div class="wordmark"><span class="dot"></span>VERTANEX®</div>
  </div>
  <div class="front-panel">
    <div class="hero-photo" role="img" aria-label="Refinery plant with chimneys at dusk"></div>
    <div class="wordmark wordmark--badge"><span class="dot"></span>VERTANEX®</div>
    <div class="front-strip">
      <svg class="facet" viewBox="0 0 578 65" preserveAspectRatio="none" aria-hidden="true">
        <rect width="578" height="65" fill="#ffffff"/>
        <polygon points="300,65 578,0 578,65" fill="#e7e8ea"/>
        <polygon points="460,65 578,20 578,65" fill="#d6262b"/>
      </svg>
      <div class="wordmark"><span class="dot"></span>VERTANEX®</div>
    </div>
  </div>
</section>

<section class="spread spread--inner">
  <div class="col col--profile">
    <h2 class="section-title">Company Profile</h2>
    <div class="photo photo--pipes-red" role="img" aria-label="Stacked red coated pipes"></div>
    <p class="body-text">Vertanex (Pte) Ltd is a Singapore based company that procures and supplies quality engineering products to oil, gas and energy sectors across the region.</p>
    <ul class="product-list">
      <li><strong>Valves and Actuators:</strong> gate, globe, ball and check valves with drives.</li>
      <li><strong>Flanges and Pipe Fittings:</strong> weld neck, blind, elbows, tees and reducers.</li>
      <li><strong>Piping and Structural:</strong> seamless pipe, plates, beams and sections.</li>
      <li><strong>Oilfield and Drilling Equipments:</strong> tools, spares and wellhead parts.</li>
    </ul>
    <p class="sub-title">Vertanex After Sales and Engineering Services (VASES) includes:</p>
    <ul class="product-list">
      <li>Fabrication, Machining and Repairing</li>
      <li>Testing, Servicing and Commissioning of Products</li>
    </ul>
    <div class="photo photo--pipes-steel" role="img" aria-label="Bundle of steel pipes seen end on"></div>
  </div>

  <div class="col col--sectors">
    <p class="kicker">Our company serves:</p>
    <p class="sector-statement">Oil &amp; Gas, Power &amp; Alternative Energy, Water Supply / Sewage, Industrial Process, Civil Infrastructure and General Construction &amp; More...</p>
    <p class="body-text">We supply products from trusted makers, checked to meet project codes and delivered on time to sites.</p>
    <p class="body-text">Our team works with clients from tender to handover, with stock held locally for fast response.</p>
    <p class="body-text">All inspections and test reports are kept for full traceability.</p>
    <p class="body-text">www.vertanex.co</p>
    <div class="sectors-foot">
      <svg class="facet" viewBox="0 0 270 250" preserveAspectRatio="none" aria-hidden="true">
        <polygon points="0,0 270,60 270,250 0,250" fill="#d9dbde"/>
        <polygon points="0,140 270,250 0,250" fill="#c9ccd0"/>
      </svg>
    </div>
  </div>

  <div class="col col--industries">
    <h2 class="band">Industries Served</h2>
    <div class="industry-grid">
      <div class="industry">
        <svg viewBox="0 0 54 54" aria-hidden="true"><path d="M27 6 C27 6 12 24 12 34 a15 15 0 0 0 30 0 C42 24 27 6 27 6z" fill="var(--blue)"/></svg>
        <h3>Oil &amp; Gas</h3>
        <ul><li>Refineries</li><li>Petrochemical plants</li><li>Offshore platforms</li><li>Pipelines</li><li>Gas terminals</li><li>Storage depots</li></ul>
      </div>
      <div class="industry">
        <svg viewBox="0 0 54 54" aria-hidden="true"><polygon points="30,4 12,30 26,30 22,50 42,22 28,22" fill="var(--blue)"/></svg>
        <h3>Power &amp; Alternative Energy</h3>
        <ul><li>Power stations</li><li>Solar farms</li><li>Wind parks</li><li>Substations</li><li>Biomass plants</li></ul>
      </div>
      <div class="industry">
        <svg viewBox="0 0 54 54" aria-hidden="true"><rect x="6" y="14" width="30" height="10" fill="var(--blue)"/><rect x="18" y="8" width="6" height="8" fill="var(--blue)"/><rect x="30" y="14" width="10" height="20" fill="var(--blue)"/><circle cx="35" cy="44" r="4" fill="var(--blue)"/></svg>
        <h3>Water Supply / Sewage</h3>
        <ul><li>Water works</li><li>Treatment plants</li><li>Pumping stations</li><li>Desalination</li><li>Drainage systems</li></ul>
      </div>
      <div class="industry">
        <svg viewBox="0 0 54 54" aria-hidden="true"><polygon points="4,48 4,26 16,18 16,26 28,18 28,26 40,18 40,8 48,8 48,48" fill="var(--blue)"/></svg>
        <h3>Industrial Process</h3>
        <ul><li>Chemical plants</li><li>Pulp and paper</li><li>Food process</li><li>Steel mills</li><li>Mining sites</li></ul>
      </div>
      <div class="industry">
        <svg viewBox="0 0 54 54" aria-hidden="true"><rect x="4" y="20" width="46" height="6" fill="var(--blue)"/><rect x="10" y="26" width="5" height="22" fill="var(--blue)"/><rect x="39" y="26" width="5" height="22" fill="var(--blue)"/><path d="M4 20 Q27 2 50 20" stroke="var(--blue)" stroke-width="4" fill="none"/></svg>
        <h3>Civil Infrastructure</h3>
        <ul><li>Bridges</li><li>Roads and rail</li><li>Ports</li><li>Airports</li><li>Tunnels</li></ul>
      </div>
      <div class="industry">
        <svg viewBox="0 0 54 54" aria-hidden="true"><rect x="8" y="14" width="16" height="34" fill="var(--blue)"/><rect x="28" y="24" width="18" height="24" fill="var(--blue)"/><rect x="4" y="48" width="46" height="3" fill="var(--blue)"/></svg>
        <h3>General Construction</h3>
        <ul><li>Commercial buildings</li><li>Residential</li><li>Warehouses</li><li>Hospitals</li><li>Schools</li></ul>
      </div>
    </div>
  </div>
</section>

</body>
</html>
```